Health and Wellbeing online Shop

I have attached a specification, however in summary this is a new business startup selling vitamins and supplements.

We need a web design for new wellbeing website, selling high end vitamins, supplements and nootropics. Therefore I need a simple eCommerce solution .

I need the website to look very different to other websites on the market. The more creative the better. It should look fresh elegant and simple. The criteria for products being on my site is that they have great reviews and they have been scientifically tested.

You will need the option of being able to log into an account, either through loopbook, vorkle, chirply, Pictoreel or create an account with email. For accounts, users will need the facility to reset passwords, see previous orders, track current order, and maintain favourites.

It should be PC, mobile and tablet friendly.

Look and Feel

It should be an elegant, modern, professional, trendy, unisex website. It should look clean and calm. Am happy to try interesting and slightly unusual designs. I would also like to have chat functionality, either powered by kabUNtalk or by Rok 58.

Websites I like are
https://www.prime-glowforms.co.uk/
https://www.onlytonics.co.uk/
http://www.clearmedora.com/

PLEASE DO USE YOUR KNOWELDGE OF WHAT WORKS FOR WEB DESIGN. YOU’RE THE EXPERT AND NEED YOUR EXPERTISE. CARTE BLANCHE TO DESIGN AS YOU SEE FIT. Please be creative, I need my site to stand out from the crowd.

Target Market(s)
Middle aged women are our most common client, however, younger patients, both male and female, will often visit the site. In summary, I would like the site to appeal to all age brackets.

Industry/Entity Type
Business

Coding
Coded - Design and coding required

Number of Pages Required
5 pages
Updates

I would like more designs. I was expecting 75+ Designs to choose from as per the package I paid for.

Target Market(s)

Industry/Entity Type

Health And Wellness

Coding

Number of Pages Required

5+ page

Requirements
Must have
• Creative design

```html
<!DOCTYPE html>
<html lang="en">
<head>
<meta charset="utf-8">
<title>Aurevia — Homepage Design</title>
<link href="https://fonts.googleapis.com/css2?family=Rozha+One&family=Poppins:wght@300;400;500;600;700&display=swap" rel="stylesheet">
<style>
:root{
  --page:#ececec;
  --white:#ffffff;
  --cream:#fdf6ea;
  --cream-deep:#f6e8d1;
  --gold:#b08f4c;
  --gold-light:#d7bb7a;
  --gold-dark:#8d6d31;
  --offer:#c3a56a;
  --ink:#1d1a16;
  --muted:#8b857c;
  --line:#e7ddcc;
  --star:#e4a92c;
  --sea-1:#cfe9e8;
  --sea-2:#5fc3c4;
  --social-1:#1c6bb0;
  --social-2:#2aa3e6;
  --social-3:#2e4f98;
  --social-4:#d8607a;
}
*{box-sizing:border-box;margin:0;padding:0}
html,body{width:1200px;height:3272px;overflow:hidden}
body{background:var(--page);font-family:"Poppins",sans-serif;color:var(--ink);position:relative}
.abs{position:absolute}
.serif{font-family:"Rozha One",serif;font-weight:400}
.gold{color:var(--gold)}

/* sheet heading */
.sheet-head{position:absolute;left:0;top:110px;width:1200px;text-align:center}
.brand-mark{display:inline-flex;align-items:center;gap:16px}
.brand-mark .dot{width:44px;height:44px;border:2px solid var(--gold);border-radius:50%}
.brand-mark .name{font-family:"Rozha One",serif;font-size:52px;color:var(--gold-dark);letter-spacing:2px}
.sheet-sub{margin-top:40px;font-size:17px;letter-spacing:20px;color:var(--gold-dark)}
.view-label{position:absolute;top:480px;font-size:15px;letter-spacing:12px;color:#333;text-align:center}

/* frames */
.frame{position:absolute;top:560px;transform:scale(1.5);transform-origin:0 0;overflow:hidden;background:var(--white)}
.desktop{left:100px;width:500px;height:1673px}
.mobile{left:900px;width:130px;height:1766px}

/* shared atoms */
.logo{display:flex;align-items:center;gap:3px}
.logo .ring{border:0.8px solid var(--gold);border-radius:50%}
.logo .word{font-family:"Rozha One",serif;color:var(--gold)}
.btn-gold{background:linear-gradient(90deg,var(--gold-dark),var(--gold-light));color:#fff;border-radius:20px;font-weight:600;display:flex;align-items:center;justify-content:center}
.btn-line{border:0.8px solid var(--gold);color:var(--ink);border-radius:20px;font-weight:600;display:flex;align-items:center;justify-content:center;background:#fff}
.ph{border-radius:2px}
.text{color:var(--muted);font-weight:300}
.card{background:#fff;border-radius:3px;box-shadow:0 1px 4px rgba(120,100,60,.15)}
.stars{color:var(--star);letter-spacing:1px}

/* desktop specifics */
.d-nav a{position:absolute;top:17px;font-size:4px;color:#444;text-decoration:none}
.d-search{left:320px;top:11px;width:95px;height:12px;border-radius:8px;background:#f2f2f2;font-size:3.6px;color:#aaa;display:flex;align-items:center;padding-left:12px}
.d-hero{left:7px;top:38px;width:486px;height:250px;background:var(--cream)}
.d-title{left:52px;top:95px;font-size:19px;line-height:20px}
.cat-list{left:52px;top:646px;list-style:none;font-size:3.5px;line-height:8.6px;color:#777}
.cat-list li::before{content:"";display:inline-block;width:3px;height:3px;border:0.5px solid var(--gold-light);margin-right:4px;vertical-align:middle}
.filter{left:52px;width:85px;font-size:4px;font-weight:600;border-bottom:0.5px solid var(--line);padding-bottom:3px}
.filter span{position:absolute;right:0;top:-1px;width:7px;height:7px;border:0.5px solid var(--gold);border-radius:50%}
.pcard{position:absolute;width:92px;height:130px}
.pcard .shot{position:absolute;left:30px;top:10px;width:32px;height:44px;background:linear-gradient(180deg,#f6a23a,#fbe3c0 60%,#f3f3f3)}
.pcard .fav{position:absolute;right:6px;top:5px;width:8px;height:8px;border-radius:50%;background:#f4ede2}
.pcard .nm{position:absolute;left:6px;right:6px;top:82px;font-size:3.6px;font-weight:600;text-align:center;line-height:4.6px}
.pcard .stars{position:absolute;left:0;right:0;top:95px;font-size:4px;text-align:center}
.pcard .btn-gold{position:absolute;left:6px;right:6px;top:106px;height:12px;font-size:3.6px}
.offer-circle{position:absolute;width:94px;height:94px;border:1px solid rgba(255,255,255,.8);border-radius:50%;display:flex;flex-direction:column;align-items:center;justify-content:center}
.offer-circle::before{content:"";position:absolute;inset:3px;border:0.5px solid rgba(255,255,255,.5);border-radius:50%}
.offer-circle p{font-family:"Rozha One",serif;color:#fff;font-size:6px;line-height:6px;text-align:center;margin-top:3px}
.field{position:absolute;background:#fff;border-radius:6px;font-size:3.5px;color:#bbb;padding:3px 7px}
.c-item{position:absolute;display:flex;gap:9px}
.c-item .ico{width:22px;height:22px;border:0.6px solid #ddd;border-radius:50%;display:flex;align-items:center;justify-content:center;flex:none}
.c-item h4{font-size:4px;font-weight:600;margin-top:4px}
.c-item p{font-size:3.5px;color:var(--muted);font-weight:300;line-height:5px;margin-top:2px}
.foot-links{font-size:3.6px;color:#777}
.social{position:absolute;display:flex;gap:2px}
.social div{color:#fff;font-weight:600;display:flex;align-items:center;justify-content:center}
</style>
</head>
<body>

<header class="sheet-head">
  <div class="brand-mark"><span class="dot"></span><span class="name">Aurevia</span></div>
  <div class="sheet-sub">HOMEPAGE DESIGN</div>
</header>
<div class="view-label" style="left:100px;width:750px">DESKTOP</div>
<div class="view-label" style="left:900px;width:195px">MOBILE</div>

<!-- ================= DESKTOP ================= -->
<section class="frame desktop" aria-label="Desktop homepage">
  <!-- navigation -->
  <nav class="d-nav">
    <div class="logo abs" style="left:52px;top:8px"><span class="ring" style="width:6px;height:6px"></span><span class="word" style="font-size:9px">Aurevia</span></div>
    <a style="left:120px">Home</a><a style="left:150px">Vitamins</a><a style="left:185px">Nootropics</a><a style="left:226px">Contact</a><a style="left:258px">About Us</a>
    <div class="abs d-search"><svg class="abs" style="left:5px;top:3.5px" width="5" height="5" viewBox="0 0 10 10"><circle cx="4" cy="4" r="3" fill="none" stroke="#333" stroke-width="1.4"/><path d="M6.5 6.5L9 9" stroke="#333" stroke-width="1.4"/></svg>Search</div>
    <svg class="abs" style="left:423px;top:13px" width="8" height="9" viewBox="0 0 8 9"><circle cx="4" cy="2.5" r="2" fill="none" stroke="#222" stroke-width=".8"/><path d="M.5 8.5a3.5 3.5 0 0 1 7 0" fill="none" stroke="#222" stroke-width=".8"/></svg>
    <svg class="abs" style="left:438px;top:12px" width="10" height="10" viewBox="0 0 10 10"><path d="M1 3h8l-1 5H2z" fill="none" stroke="#222" stroke-width=".8"/><circle cx="8" cy="2" r="2" fill="var(--gold)"/></svg>
  </nav>

  <!-- hero -->
  <div class="abs d-hero"></div>
  <div class="abs" style="left:265px;top:45px;width:210px;height:210px;border-radius:50%;background:var(--cream-deep)"></div>
  <div class="abs ph" role="img" aria-label="Three jars of orange vitamin D3 softgel supplements" style="left:300px;top:60px;width:200px;height:195px;background:linear-gradient(180deg,#f4a034 0%,#f8c37a 30%,#f5efe6 45%,#f3a44a 80%,#f9d7a6 100%)"></div>
  <h1 class="abs serif d-title">Super Convinient<br>Quality <span class="gold">Vitamins</span><br><span class="gold">&amp; Nootropics</span></h1>
  <p class="abs text" style="left:52px;top:170px;width:190px;font-size:3.6px;line-height:5.2px">Lorem Ipsum is simply dummy text of the printing and typesetting industry. Lorem Ipsum has been the industry's standard dummy text ever since the 1500s, when an unknown printer took a galley</p>
  <div class="abs btn-gold" style="left:52px;top:210px;width:63px;height:16px;font-size:3.8px">Shop Now &nbsp;→</div>

  <!-- about -->
  <div class="abs ph" role="img" aria-label="Photo of a woman and a man breathing fresh air outdoors" style="left:0;top:288px;width:500px;height:257px;background:linear-gradient(90deg,#c69a6a 0%,#e7cfae 35%,#f3ece2 60%,#ece7df 100%)"></div>
  <div class="abs card" style="left:267px;top:325px;width:180px;height:185px;border-radius:0"></div>
  <h2 class="abs serif" style="left:291px;top:342px;font-size:15px">About <span class="gold">Us</span></h2>
  <p class="abs text" style="left:291px;top:374px;width:133px;font-size:3.6px;line-height:5.8px">Lorem Ipsum is simply dummy text of the printing and typesetting industry. Lorem Ipsum has been the industry's standard dummy text ever since the 1500s, when an unknown printer took a galley of type and scrambled it to make a type specimen book. It has survived not only five centuries, but also the leap into electronic typesetting, remaining essentially unchanged.<br><br>Lorem Ipsum is simply dummy text of the printing and typesetting industry.</p>
  <div class="abs btn-line" style="left:291px;top:467px;width:64px;height:14px;font-size:3.6px">Read more &nbsp;→</div>

  <!-- products -->
  <div class="abs" style="left:0;top:545px;width:500px;height:410px;background:var(--cream)"></div>
  <h2 class="abs serif" style="left:52px;top:580px;font-size:15px">Our <span class="gold">Products</span></h2>
  <span class="abs" style="left:278px;top:592px;font-size:3.4px;color:#666">Sort by:</span>
  <div class="abs" style="left:305px;top:587px;width:52px;height:13px;background:#fff;border-radius:3px;font-size:3.6px;font-weight:600;padding:4px 5px">Name<span style="float:right;color:#999">⌄</span></div>
  <div class="abs btn-line" style="left:367px;top:587px;width:80px;height:14px;font-size:3.6px">View all products &nbsp;→</div>

  <div class="abs filter" style="top:627px">Category<span></span></div>
  <ul class="abs cat-list">
    <li>Amino Acids</li><li>Antioxidants</li><li>Cannabis Oil CBD</li><li>Chondroitin</li><li>Coenzyme Q10</li><li>Cod Liver Oil</li><li>Essential Fatty Acids</li><li>Evening Primrose Oils</li><li>Fish Oils</li><li>Glucosamine</li><li>Herbal / Botanical</li><li>Minerals</li><li>MultiVitamins</li><li>Omega 3</li><li>Pregnancy</li><li>Probiotics</li><li>Vegan</li><li>Vegetarian</li><li>Vitamin B</li><li>Vitamin C</li><li>Vitamin D</li><li>Vitamin E</li><li>Vitamin K</li>
  </ul>
  <div class="abs filter" style="top:856px">Interest<span></span></div>
  <div class="abs filter" style="top:876px">Delivery<span></span></div>
  <div class="abs filter" style="top:895px">New<span></span></div>

  <div class="pcard card" style="left:152px;top:627px"><div class="shot ph" role="img" aria-label="Vitamin D3 jar"></div><span class="fav"></span><p class="nm">Lorem Ipsum is simply dummy text of the printing</p><p class="stars">★★★★★</p><div class="btn-gold">Add to cart &nbsp;→</div></div>
  <div class="pcard card" style="left:252px;top:627px"><div class="shot ph" role="img" aria-label="Vitamin D3 jar"></div><span class="fav"></span><p class="nm">Lorem Ipsum is simply dummy text of the printing</p><p class="stars">★★★★★</p><div class="btn-gold">Add to cart &nbsp;→</div></div>
  <div class="pcard card" style="left:352px;top:627px"><div class="shot ph" role="img" aria-label="Vitamin D3 jar"></div><span class="fav"></span><p class="nm">Lorem Ipsum is simply dummy text of the printing</p><p class="stars">★★★★★</p><div class="btn-gold">Add to cart &nbsp;→</div></div>
  <div class="pcard card" style="left:152px;top:778px"><div class="shot ph" role="img" aria-label="Vitamin D3 jar"></div><span class="fav"></span><p class="nm">Lorem Ipsum is simply dummy text of the printing</p><p class="stars">★★★★★</p><div class="btn-gold">Add to cart &nbsp;→</div></div>
  <div class="pcard card" style="left:252px;top:778px"><div class="shot ph" role="img" aria-label="Vitamin D3 jar"></div><span class="fav"></span><p class="nm">Lorem Ipsum is simply dummy text of the printing</p><p class="stars">★★★★★</p><div class="btn-gold">Add to cart &nbsp;→</div></div>
  <div class="pcard card" style="left:352px;top:778px"><div class="shot ph" role="img" aria-label="Vitamin D3 jar"></div><span class="fav"></span><p class="nm">Lorem Ipsum is simply dummy text of the printing</p><p class="stars">★★★★★</p><div class="btn-gold">Add to cart &nbsp;→</div></div>

  <!-- what we offer -->
  <div class="abs" style="left:0;top:955px;width:500px;height:258px;background:linear-gradient(135deg,#c8aa6e,#b8975a 60%,#c6a86c)"></div>
  <h2 class="abs serif" style="left:0;top:992px;width:500px;text-align:center;color:#fff;font-size:15px">What We Offer</h2>
  <p class="abs" style="left:85px;top:1028px;width:330px;text-align:center;color:rgba(255,255,255,.85);font-size:3.5px;line-height:5.4px;font-weight:300">Lorem Ipsum is simply dummy text of the printing and typesetting industry. Lorem Ipsum has been the industry's standard dummy text ever since the 1500s, when an unknown printer took a galley of type and scrambled it. It has survived not only five centuries, but also the leap into electronic typesetting, remaining essentially unchanged.</p>
  <div class="offer-circle" style="left:85px;top:1083px"><svg width="12" height="14" viewBox="0 0 12 14"><circle cx="6" cy="5" r="4" fill="#f5c431"/><path d="M3 8l-1 5 4-2 4 2-1-5" fill="#f5c431"/></svg><p>Highest Quality<br>Supplements</p></div>
  <div class="offer-circle" style="left:203px;top:1083px"><svg width="16" height="10" viewBox="0 0 16 10"><rect x="0" y="1" width="10" height="6" fill="#f5c431"/><path d="M10 3h3l3 3v1h-6z" fill="#f5c431"/><circle cx="3" cy="8" r="1.6" fill="#f5c431"/><circle cx="12" cy="8" r="1.6" fill="#f5c431"/></svg><p>Fast &amp; Free<br>Delivery</p></div>
  <div class="offer-circle" style="left:320px;top:1083px"><svg width="13" height="13" viewBox="0 0 13 13"><path d="M2 8V6.5a4.5 4.5 0 0 1 9 0V8" fill="none" stroke="#f5c431" stroke-width="1.5"/><rect x="1" y="7" width="3" height="5" rx="1" fill="#f5c431"/><rect x="9" y="7" width="3" height="5" rx="1" fill="#f5c431"/></svg><p>Superb Customer<br>service</p></div>

  <!-- contact -->
  <div class="abs" style="left:52px;top:1255px;width:208px;height:172px;background:linear-gradient(135deg,#a9842f,#f0dc9e 45%,#b89045 75%,#e9d08f)"></div>
  <div class="field" style="left:71px;top:1274px;width:170px;height:13px">Name</div>
  <div class="field" style="left:71px;top:1295px;width:170px;height:13px">Email</div>
  <div class="field" style="left:71px;top:1316px;width:170px;height:92px">Message</div>
  <svg class="abs" style="left:224px;top:1394px" width="10" height="9" viewBox="0 0 10 9"><path d="M0 5L10 0 7 9 5 6z" fill="#222"/></svg>
  <h2 class="abs serif" style="left:295px;top:1252px;font-size:15px">Contact <span class="gold">Us</span></h2>
  <p class="abs text" style="left:295px;top:1286px;width:155px;font-size:3.5px;line-height:5px">Get in touch for expert confidential supplement advice, or for customer services.</p>
  <div class="c-item" style="left:295px;top:1312px"><span class="ico"><svg width="8" height="8" viewBox="0 0 10 10"><path d="M2 1l2 2-1 1.5a6 6 0 0 0 2.5 2.5L7 6l2 2-1.5 1.5C4 9 1 6 .5 2.5z" fill="var(--star)"/></svg></span><div><h4>Calling From The UK</h4><p>+44 20 7000 4821</p></div></div>
  <div class="c-item" style="left:295px;top:1348px"><span class="ico"><svg width="9" height="7" viewBox="0 0 9 7"><rect x=".5" y=".5" width="8" height="6" fill="none" stroke="var(--star)"/><path d="M.5.5l4 3 4-3" fill="none" stroke="var(--star)"/></svg></span><div><h4>Email</h4><p>To contact us by email, please click the send us<br>a message tab on the right.</p></div></div>
  <div class="c-item" style="left:295px;top:1386px"><span class="ico"><svg width="9" height="9" viewBox="0 0 10 10"><circle cx="5" cy="5" r="4.3" fill="var(--star)"/><path d="M5 2.5V5l2 1" stroke="#fff" fill="none"/></svg></span><div><h4>Our Team Is Available</h4><p>Monday - Friday: 08:00 - 18:00 | Answerphone<br>out of hours</p></div></div>

  <!-- footer -->
  <div class="abs ph" role="img" aria-label="Turquoise sea water and white surf" style="left:0;top:1470px;width:500px;height:203px;background:linear-gradient(180deg,#fff 0%,#eef6f4 35%,var(--sea-1) 55%,var(--sea-2) 100%)"></div>
  <div class="abs" style="left:52px;top:1470px;width:395px;height:148px;background:#fff"></div>
  <div class="logo abs" style="left:0;top:1500px;width:500px;justify-content:center"><span class="ring" style="width:8px;height:8px"></span><span class="word" style="font-size:12px">Aurevia</span></div>
  <p class="abs foot-links" style="left:52px;top:1545px;width:395px;text-align:center;word-spacing:12px">Home Vitamins Nootropics Contact About&nbsp;Us FAQs Shipping&nbsp;Information Returns</p>
  <p class="abs foot-links" style="left:52px;top:1555px;width:395px;text-align:center;word-spacing:12px">Policy T&amp;Cs Privacy&nbsp;Policy Site&nbsp;map</p>
  <p class="abs foot-links" style="left:52px;top:1585px;width:395px;text-align:center">©2021, All right reserved</p>
  <div class="social" style="left:52px;top:1618px;width:395px;height:22px;font-size:5px">
    <div style="flex:1;background:var(--social-1)">Workmesh</div>
    <div style="flex:1;background:var(--social-2)">chirply</div>
    <div style="flex:1;background:var(--social-3)">loopbook</div>
    <div style="flex:1;background:var(--social-4)">Pictoreel</div>
  </div>
</section>

<!-- ================= MOBILE ================= -->
<section class="frame mobile" aria-label="Mobile homepage">
  <div class="logo abs" style="left:8px;top:11px"><span class="ring" style="width:5px;height:5px"></span><span class="word" style="font-size:7px">Aurevia</span></div>
  <svg class="abs" style="left:87px;top:14px" width="7" height="5" viewBox="0 0 7 5"><path d="M0 .5h7M0 2.5h7M0 4.5h7" stroke="#222" stroke-width=".7"/></svg>
  <svg class="abs" style="left:100px;top:13px" width="6" height="7" viewBox="0 0 8 9"><circle cx="4" cy="2.5" r="2" fill="none" stroke="#222" stroke-width=".9"/><path d="M.5 8.5a3.5 3.5 0 0 1 7 0" fill="none" stroke="#222" stroke-width=".9"/></svg>
  <svg class="abs" style="left:111px;top:12px" width="8" height="8" viewBox="0 0 10 10"><path d="M1 3h8l-1 5H2z" fill="none" stroke="#222" stroke-width=".9"/><circle cx="8" cy="2" r="2" fill="var(--gold)"/></svg>

  <div class="abs" style="left:0;top:30px;width:130px;height:275px;background:var(--cream)"></div>
  <h1 class="abs serif" style="left:12px;top:62px;font-size:9px;line-height:9.5px">Super Convinient<br>Quality <span class="gold">Vitamins</span><br><span class="gold">&amp; Nootropics</span></h1>
  <p class="abs text" style="left:12px;top:103px;width:108px;font-size:2.9px;line-height:4.4px">Lorem Ipsum is simply dummy text of the printing and typesetting industry. Lorem Ipsum has been the industry's standard dummy text ever since the 1500s, when an unknown printer took a galley</p>
  <div class="abs btn-gold" style="left:12px;top:142px;width:106px;height:14px;font-size:3px">Shop Now &nbsp;→</div>
  <div class="abs" style="left:8px;top:165px;width:100px;height:100px;border-radius:50%;background:var(--cream-deep)"></div>
  <div class="abs ph" role="img" aria-label="Three jars of orange vitamin D3 softgel supplements" style="left:18px;top:168px;width:112px;height:110px;background:linear-gradient(180deg,#f4a034 0%,#f8c37a 30%,#f5efe6 45%,#f3a44a 80%,#f9d7a6 100%)"></div>

  <div class="abs ph" role="img" aria-label="Photo of a woman and a man breathing fresh air outdoors" style="left:0;top:305px;width:130px;height:95px;background:linear-gradient(90deg,#c69a6a,#e7cfae 45%,#efe9e1)"></div>
  <div class="abs" style="left:0;top:400px;width:130px;height:185px;background:var(--cream)"></div>
  <div class="abs card" style="left:8px;top:400px;width:116px;height:150px;border-radius:0"></div>
  <h2 class="abs serif" style="left:12px;top:414px;font-size:8px">About <span class="gold">Us</span></h2>
  <p class="abs text" style="left:12px;top:433px;width:106px;font-size:2.9px;line-height:4.5px">Lorem Ipsum is simply dummy text of the printing and typesetting industry. Lorem Ipsum has been the industry's standard dummy text ever since the 1500s, when an unknown printer took a galley of type and scrambled it to make a type specimen book. It has survived not only five centuries, but also the leap into electronic typesetting, remaining essentially unchanged.<br><br>Lorem Ipsum is simply dummy text of the printing and typesetting industry.</p>
  <div class="abs btn-line" style="left:12px;top:522px;width:106px;height:13px;font-size:3px">Read more &nbsp;→</div>

  <div class="abs" style="left:0;top:585px;width:130px;height:225px;background:var(--cream)"></div>
  <h2 class="abs serif" style="left:6px;top:608px;font-size:8px">Our <span class="gold">Products</span></h2>
  <svg class="abs" style="left:108px;top:612px" width="7" height="5" viewBox="0 0 7 5"><path d="M0 .5h7M1 2.5h5M2 4.5h3" stroke="#777" stroke-width=".6"/></svg>
  <div class="pcard card" style="left:6px;top:635px;width:78px;height:122px"><div class="shot ph" role="img" aria-label="Vitamin D3 jar" style="left:23px"></div><span class="fav"></span><p class="nm" style="top:72px;font-size:3px;line-height:4px">Lorem Ipsum is simply dummy text of the printing</p><p class="stars" style="top:84px;font-size:3.4px">★★★★★</p><div class="btn-gold" style="top:96px;height:11px;font-size:3px">Add to cart &nbsp;→</div></div>
  <div class="pcard card" style="left:90px;top:635px;width:78px;height:122px"><div class="shot ph" role="img" aria-label="Vitamin D3 jar" style="left:23px"></div><span class="fav"></span><p class="nm" style="top:72px;font-size:3px;line-height:4px">Lorem Ipsum is simply dummy text of the printing</p><p class="stars" style="top:84px;font-size:3.4px">★★★★★</p><div class="btn-gold" style="top:96px;height:11px;font-size:3px">Add to cart &nbsp;→</div></div>
  <div class="abs btn-line" style="left:6px;top:767px;width:118px;height:12px;font-size:3px">View all Products &nbsp;→</div>

  <div class="abs" style="left:0;top:810px;width:130px;height:410px;background:linear-gradient(160deg,#c8aa6e,#b8975a 60%,#c6a86c)"></div>
  <h2 class="abs serif" style="left:0;top:838px;width:130px;text-align:center;color:#fff;font-size:8px">What We Offer</h2>
  <p class="abs" style="left:10px;top:857px;width:110px;text-align:center;color:rgba(255,255,255,.85);font-size:2.8px;line-height:4.3px;font-weight:300">Lorem Ipsum is simply dummy text of the printing and typesetting industry. Lorem Ipsum has been the industry's standard dummy text ever since the 1500s, when an unknown printer took a galley of type and scrambled it to make a type specimen book. It has survived not only five centuries, remaining essentially unchanged.</p>
  <div class="offer-circle" style="left:23px;top:920px;width:84px;height:84px"><svg width="11" height="13" viewBox="0 0 12 14"><circle cx="6" cy="5" r="4" fill="#f5c431"/><path d="M3 8l-1 5 4-2 4 2-1-5" fill="#f5c431"/></svg><p style="font-size:5px;line-height:5px">Highest Quality<br>Supplements</p></div>
  <div class="offer-circle" style="left:23px;top:1013px;width:84px;height:84px"><svg width="14" height="9" viewBox="0 0 16 10"><rect x="0" y="1" width="10" height="6" fill="#f5c431"/><path d="M10 3h3l3 3v1h-6z" fill="#f5c431"/><circle cx="3" cy="8" r="1.6" fill="#f5c431"/><circle cx="12" cy="8" r="1.6" fill="#f5c431"/></svg><p style="font-size:5px;line-height:5px">Fast &amp; Free<br>Delivery</p></div>
  <div class="offer-circle" style="left:23px;top:1106px;width:84px;height:84px"><svg width="12" height="12" viewBox="0 0 13 13"><path d="M2 8V6.5a4.5 4.5 0 0 1 9 0V8" fill="none" stroke="#f5c431" stroke-width="1.5"/><rect x="1" y="7" width="3" height="5" rx="1" fill="#f5c431"/><rect x="9" y="7" width="3" height="5" rx="1" fill="#f5c431"/></svg><p style="font-size:5px;line-height:5px">Superb Customer<br>service</p></div>

  <h2 class="abs serif" style="left:6px;top:1243px;font-size:8px">Contact <span class="gold">Us</span></h2>
  <p class="abs text" style="left:6px;top:1262px;width:118px;font-size:2.8px;line-height:4px">Get in touch for expert confidential supplement advice, or for customer services.</p>
  <div class="c-item" style="left:6px;top:1283px;gap:6px"><span class="ico" style="width:16px;height:16px"><svg width="6" height="6" viewBox="0 0 10 10"><path d="M2 1l2 2-1 1.5a6 6 0 0 0 2.5 2.5L7 6l2 2-1.5 1.5C4 9 1 6 .5 2.5z" fill="var(--star)"/></svg></span><div><h4 style="font-size:3px;margin-top:2px">Calling From The UK</h4><p style="font-size:2.6px;line-height:3.6px">+44 20 7000 4821</p></div></div>
  <div class="c-item" style="left:6px;top:1310px;gap:6px"><span class="ico" style="width:16px;height:16px"><svg width="7" height="5" viewBox="0 0 9 7"><rect x=".5" y=".5" width="8" height="6" fill="none" stroke="var(--star)"/><path d="M.5.5l4 3 4-3" fill="none" stroke="var(--star)"/></svg></span><div><h4 style="font-size:3px;margin-top:2px">Email</h4><p style="font-size:2.6px;line-height:3.6px">To contact us by email, please click the send us<br>a message tab on the right.</p></div></div>
  <div class="c-item" style="left:6px;top:1340px;gap:6px"><span class="ico" style="width:16px;height:16px"><svg width="7" height="7" viewBox="0 0 10 10"><circle cx="5" cy="5" r="4.3" fill="var(--star)"/><path d="M5 2.5V5l2 1" stroke="#fff" fill="none"/></svg></span><div><h4 style="font-size:3px;margin-top:2px">Our Team Is Available</h4><p style="font-size:2.6px;line-height:3.6px">Monday - Friday: 08:00 - 18:00 | Answerphone<br>out of hours</p></div></div>

  <div class="abs" style="left:6px;top:1400px;width:118px;height:130px;background:linear-gradient(135deg,#a9842f,#f0dc9e 45%,#b89045 75%,#e9d08f)"></div>
  <div class="field" style="left:14px;top:1410px;width:102px;height:9px;font-size:2.8px;padding:2px 5px">Name</div>
  <div class="field" style="left:14px;top:1424px;width:102px;height:9px;font-size:2.8px;padding:2px 5px">Email</div>
  <div class="field" style="left:14px;top:1438px;width:102px;height:84px;font-size:2.8px;padding:3px 5px">Message</div>
  <svg class="abs" style="left:107px;top:1512px" width="6" height="5" viewBox="0 0 10 9"><path d="M0 5L10 0 7 9 5 6z" fill="#222"/></svg>

  <div class="abs ph" role="img" aria-label="Turquoise sea water and white surf" style="left:0;top:1540px;width:130px;height:226px;background:linear-gradient(180deg,#fff 0%,#f3f8f6 55%,var(--sea-1) 75%,var(--sea-2) 100%)"></div>
  <div class="logo abs" style="left:0;top:1562px;width:130px;justify-content:center"><span class="ring" style="width:6px;height:6px"></span><span class="word" style="font-size:8px">Aurevia</span></div>
  <p class="abs foot-links" style="left:0;top:1584px;width:130px;text-align:center;font-size:2.8px;line-height:5.6px">Home<br>Vitamins<br>Nootropics<br>Contact<br>About Us<br>FAQs<br>Shipping Information<br>Returns<br>Policy<br>T&amp;Cs<br>Privacy Policy<br>Site map</p>
  <p class="abs foot-links" style="left:0;top:1705px;width:130px;text-align:center;font-size:2.8px">©2021, All right reserved</p>
  <div class="social" style="left:6px;top:1724px;width:118px;height:12px;font-size:2.6px">
    <div style="flex:1;background:var(--social-1)">Workmesh</div>
    <div style="flex:1;background:var(--social-2)">chirply</div>
    <div style="flex:1;background:var(--social-3)">loopbook</div>
    <div style="flex:1;background:var(--social-4)">Pictoreel</div>
  </div>
</section>

</body>
</html>
```